Create a flyer design (10cm X 21cm) for an aquarium in France

We are a public aquarium in France and we want announcing the events of christmas holidays
We invite you to create our flyer recto (just the front side).

The size of this flyer is : 10cm X 21cm
Have a look on flyer.doc to know texts...
We want also get the flyer in original version (.psd, .ai) please.

We remain at your disposal for any question.
Thanks.

• The text must be written in french, you will find attached all the text that you have to fill in the flyer.
• You also have to use our logo in the top or in the bottom of the flyer (2 versions of the logo four color or black and white version. According your design you can use one of them)
• You must specify our website and our adress.
• Have a look on flyer.doc to know texts...

```html
<!DOCTYPE html>
<html lang="fr">
<head>
<meta charset="utf-8">
<title>Noël à l'aquarium</title>
<link rel="stylesheet" href="https://fonts.googleapis.com/css2?family=Bree+Serif&family=Dosis:wght@500;600;700&display=swap">
<style>
  :root {
    --ink-sea: #1c4f82;
    --deep-sea: #123e6c;
    --footer-sea: #143a63;
    --white: #ffffff;
    --xmas-red: #e31b4b;
    --sky-blue: #2f86c9;
    --light-blue: #5cc3ee;
    --lime: #b5d334;
    --leaf-green: #8fcf4e;
    --orange: #f39a1e;
    --title-blue: #1b4a7e;
  }
  * { margin: 0; padding: 0; box-sizing: border-box; }
  html, body { width: 1200px; height: 2522px; overflow: hidden; background: var(--white); }
  .flyer {
    position: relative; width: 1200px; height: 2522px; overflow: hidden;
    background: linear-gradient(180deg, var(--ink-sea) 0%, var(--deep-sea) 100%);
    font-family: "Bree Serif", Georgia, serif; color: var(--white);
  }
  .abs { position: absolute; }
  .nowrap { white-space: nowrap; }
  .header-wave { left: 0; top: 0; width: 1200px; height: 520px; }
  .info-line {
    left: 0; top: 70px; width: 1200px; text-align: center;
    font-family: "Dosis", Arial, sans-serif; font-weight: 600; font-size: 40px;
    letter-spacing: 2px; color: var(--title-blue);
  }
  .info-line span { color: var(--xmas-red); }
  .title {
    left: 0; top: 168px; width: 1200px; text-align: center;
    font-size: 162px; line-height: 138px; font-weight: 400; -webkit-text-stroke: 2px currentColor;
  }
  .title .red { color: var(--xmas-red); display: block; }
  .title .blue { color: var(--title-blue); display: block; }

  .art-santa {
    left: 40px; top: 480px; width: 680px; height: 640px; border-radius: 40% 45% 35% 40%;
    background: radial-gradient(circle at 45% 40%, #d8233f 0%, #b41d3a 35%, rgba(60,150,200,0.55) 70%, rgba(28,79,130,0) 100%);
  }
  .art-fish-left { left: 40px; top: 1060px; width: 260px; height: 190px; border-radius: 50%;
    background: radial-gradient(circle, rgba(243,154,30,0.8) 0%, rgba(243,154,30,0) 70%); }
  .art-fish-right { left: 880px; top: 1110px; width: 300px; height: 180px; border-radius: 50%;
    background: radial-gradient(circle, rgba(181,211,52,0.7) 0%, rgba(181,211,52,0) 70%); }
  .art-seahorse { left: 1045px; top: 1790px; width: 145px; height: 510px; border-radius: 45%;
    background: radial-gradient(ellipse at 50% 45%, rgba(170,205,80,0.85) 0%, rgba(120,170,70,0.5) 45%, rgba(28,79,130,0) 75%); }

  .activities { left: 740px; top: 500px; width: 450px; }
  .activity { font-size: 48px; line-height: 52px; white-space: nowrap; -webkit-text-stroke: 1px currentColor; }
  .tag {
    display: inline-block; background: var(--xmas-red); color: var(--white);
    font-family: "Dosis", Arial, sans-serif; font-weight: 700; font-size: 50px; line-height: 50px;
    padding: 4px 12px; margin: 8px 0 14px;
  }
  .dive-title {
    left: 428px; top: 1112px; font-size: 76px; line-height: 68px; color: var(--xmas-red);
    transform: rotate(-3deg); transform-origin: left top; white-space: nowrap; -webkit-text-stroke: 1px currentColor;
  }

  .month { font-family: "Dosis", Arial, sans-serif; font-weight: 500; font-size: 27px; letter-spacing: 3px; color: var(--light-blue); }
  .day {
    position: absolute; width: 125px; background: var(--sky-blue);
    font-family: "Dosis", Arial, sans-serif; color: rgba(255,255,255,0.85);
  }
  .day .dname { position: absolute; left: 8px; top: 4px; font-size: 19px; font-weight: 600; letter-spacing: 1px; }
  .day .dnum { position: absolute; left: 0; right: 0; bottom: 2px; text-align: center; font-size: 88px; font-weight: 500; line-height: 98px; }
  .row1 { top: 1315px; height: 120px; }
  .row2 { top: 1452px; height: 144px; }
  .row2 .dnum, .jan .dnum { font-weight: 700; color: var(--deep-sea); }
  .jan { top: 1507px; height: 132px; width: 130px; }
  .is-red { background: var(--xmas-red); color: var(--white); }
  .is-red .dnum { font-weight: 700; }
  .is-light { background: var(--light-blue); }
  .is-green { background: linear-gradient(180deg, var(--lime) 60%, #8fc2a0 100%); }
  .is-orange { background: var(--orange); }
  .is-lime { background: var(--lime); }

  .links { left: 0; top: 0; width: 1200px; height: 2522px; pointer-events: none; }

  .event-head { font-size: 70px; line-height: 62px; white-space: nowrap; -webkit-text-stroke: 1px currentColor; }
  .event-sub { font-size: 42px; line-height: 44px; white-space: nowrap; margin-top: 4px; }
  .nocturne { left: 168px; top: 1686px; }
  .nocturne .event-sub { margin-left: 52px; }
  .nocturne .event-head { color: var(--leaf-green); }
  .tasting { left: 744px; top: 1684px; }
  .tasting .event-head { color: var(--lime); }
  .workshop { left: 53px; top: 1934px; }
  .workshop .event-head { color: var(--light-blue); }
  .manicure { left: 468px; top: 1925px; }
  .manicure .event-head { color: var(--orange); }
  .manicure em { font-style: italic; }

  .footer { left: 0; top: 2222px; width: 1200px; height: 300px; background: var(--footer-sea); }
  .brand { left: 60px; top: 2262px; width: 500px; text-align: center; font-size: 70px; line-height: 78px; color: var(--light-blue); }
  .address { left: 588px; top: 2248px; font-size: 40px; line-height: 56px; font-style: normal; white-space: nowrap; }
  .address strong { font-weight: 400; -webkit-text-stroke: 1px currentColor; }
  .phone { left: 588px; top: 2406px; font-family: "Dosis", Arial, sans-serif; font-weight: 700; font-size: 76px; line-height: 90px; color: var(--lime); }
</style>
</head>
<body>
<div class="flyer">
  <svg class="abs header-wave" viewBox="0 0 1200 520" aria-hidden="true">
    <path d="M0 0 H1200 V455 C1110 495 1020 430 930 470 C840 510 760 440 660 475 C560 510 470 445 370 478 C270 510 180 445 90 475 C50 488 20 485 0 478 Z" fill="#ffffff"/>
  </svg>

  <p class="abs info-line">TOUTES LES INFORMATIONS VIA <span>AQUARIUMDEKERBRUNE.FR</span></p>
  <h1 class="abs title"><span class="red">Noël</span><span class="blue">à l’aquarium</span></h1>

  <div class="abs art-santa" role="img" aria-label="Illustration du Père-Noël en plongeur avec bouteille, palmes et bulles"></div>
  <div class="abs art-fish-left" role="img" aria-label="Illustration de petits poissons orange"></div>
  <div class="abs art-fish-right" role="img" aria-label="Illustration de poissons verts"></div>

  <div class="abs activities">
    <p class="activity">Animations<br>«bassin tactile»<br>commentées</p>
    <span class="tag">PLUSIEURS<br>FOIS PAR JOUR</span>
    <p class="activity">Nourrissages<br>commentés<br>de nos espèces<br>aquatiques</p>
    <span class="tag">CHAQUE<br>APRÈS-MIDI</span>
  </div>

  <p class="abs dive-title">Plongée<br>du Père-Noël</p>

  <p class="abs month" style="left:120px; top:1276px;">DÉCEMBRE 2015</p>
  <div class="day row1" style="left:120px;"><span class="dname">LUN</span><span class="dnum">21</span></div>
  <div class="day row1 is-red" style="left:257px;"><span class="dname">MAR</span><span class="dnum">22</span></div>
  <div class="day row1 is-red" style="left:394px;"><span class="dname">MER</span><span class="dnum">23</span></div>
  <div class="day row1" style="left:530px;"><span class="dname">JEU</span><span class="dnum">24</span></div>
  <div class="day row1" style="left:667px;"><span class="dname">VEN</span><span class="dnum">25</span></div>
  <div class="day row1" style="left:804px;"><span class="dname">SAM</span><span class="dnum">26</span></div>
  <div class="day row1" style="left:941px;"><span class="dname">DIM</span><span class="dnum">27</span></div>

  <div class="day row2 is-light" style="left:120px;"><span class="dname">LUN</span><span class="dnum">28</span></div>
  <div class="day row2 is-green" style="left:257px;"><span class="dname">MAR</span><span class="dnum">29</span></div>
  <div class="day row2 is-orange" style="left:394px;"><span class="dname">MER</span><span class="dnum">30</span></div>
  <div class="day row2 is-orange" style="left:530px; width:115px;"><span class="dname">JEU</span><span class="dnum">31</span></div>

  <p class="abs month" style="left:680px; top:1462px;">JANVIER 2016</p>
  <div class="day jan" style="left:677px;"><span class="dname">VEN</span><span class="dnum">1</span></div>
  <div class="day jan is-lime" style="left:816px;"><span class="dname">SAM</span><span class="dnum">2</span></div>
  <div class="day jan is-lime" style="left:955px;"><span class="dname">DIM</span><span class="dnum">3</span></div>

  <svg class="abs links" viewBox="0 0 1200 2522" aria-hidden="true">
    <g fill="none" stroke-width="4" stroke-dasharray="10 10">
      <path d="M182 1600 C170 1720 110 1830 96 1925" stroke="#5cc3ee"/>
      <path d="M320 1600 C330 1630 285 1655 280 1684" stroke="#8fcf4e"/>
      <path d="M456 1600 C530 1700 590 1800 624 1915" stroke="#f39a1e"/>
      <path d="M880 1642 L880 1680" stroke="#b5d334"/>
    </g>
  </svg>

  <div class="abs nocturne">
    <p class="event-head">Nocturne</p>
    <p class="event-sub">une visite drôle<br>et décalée dès 18h30</p>
  </div>
  <div class="abs tasting">
    <p class="event-head">Dégustation<br>vitaminée</p>
    <p class="event-sub">à base<br>de spiruline!</p>
  </div>
  <div class="abs workshop">
    <p class="event-head">Atelier<br>scientifique</p>
    <p class="event-sub">sur les Requins<br>pour les 6 – 12 ans</p>
  </div>
  <div class="abs manicure">
    <p class="event-head">Fish manucure</p>
    <p class="event-sub">un instant beauté<br>original avec les<br><em>Garra rufa</em>, nos poissons<br>experts en manucure !</p>
  </div>

  <div class="abs footer"></div>
  <div class="abs art-seahorse" role="img" aria-label="Illustration d’un hippocampe portant un bonnet de Noël"></div>
  <p class="abs brand">Aquarium de Kerbrune</p>
  <address class="abs address">
    <strong>Aquarium de Kerbrune</strong><br>14, rue des Goélands<br>56999 KERBRUNE
  </address>
  <p class="abs phone">02 90 11 23 45</p>
</div>
</body>
</html>
```